Banner Ad Design

Need design of small banners for page margins on a Printing website that is currently under development. Need designs for these 4 promo items:

Table Tents (1000): $217
Flyers (5000): $328
Postcards (5000): $237
Brochures (5000): $386

Use the same detail text that is shown in the attached examples - such as "Full Color Front 14 pt, etc, etc". Pricing and quantity should be as provided above.

Color scheme and images should also be similar to what is shown. Banner sizes should be 120 x 120.

```html
<!DOCTYPE html>
<html lang="en">
<head>
<meta charset="utf-8">
<title>Print Specials Banners</title>
<link rel="stylesheet" href="https://fonts.googleapis.com/css2?family=Archivo+Black&family=Roboto:wght@900&display=swap">
<style>
  :root {
    --page-bg: #ffffff;
    --tile-top: #f4f4f4;
    --tile-bottom: #c9c9c9;
    --tile-edge: #b5b5b5;
    --ribbon: #e8561a;
    --ribbon-dark: #b8400f;
    --label-orange: #f2700f;
    --outline: #111111;
    --price-green-light: #4fc42a;
    --price-green-dark: #1f7d10;
    --price-rim: #0f4a07;
    --white: #ffffff;
  }
  * { box-sizing: border-box; margin: 0; padding: 0; }
  html, body { width: 1200px; height: 300px; overflow: hidden; background: var(--page-bg); }
  .banner-strip { position: relative; width: 1200px; height: 300px; }
  .promo-tile {
    position: absolute; top: 10px; width: 281px; height: 280px;
    border-radius: 16px; overflow: hidden;
    background: linear-gradient(180deg, var(--tile-top) 0%, var(--tile-bottom) 100%);
    box-shadow: inset 0 0 0 1px var(--tile-edge);
  }
  .promo-tile:nth-child(1) { left: 10px; }
  .promo-tile:nth-child(2) { left: 313px; }
  .promo-tile:nth-child(3) { left: 616px; }
  .promo-tile:nth-child(4) { left: 909px; }

  .product-visual { position: absolute; z-index: 1; border-radius: 4px; box-shadow: 2px 3px 6px rgba(0,0,0,.35); }
  .visual-tent { left: 60px; top: 14px; width: 150px; height: 240px; background: linear-gradient(160deg, #fbfaf6, #e4e0d6); }
  .visual-flyers { left: 18px; top: 14px; width: 245px; height: 215px; background: linear-gradient(110deg, #1d1d22 0%, #7bbf2c 45%, #d7d2cc 75%, #2a2a30 100%); }
  .visual-postcards { left: 18px; top: 14px; width: 250px; height: 215px; background: linear-gradient(135deg, #6d8aa6 0%, #7b9a58 40%, #c28a4a 70%, #3a2a22 100%); }
  .visual-brochures { left: 40px; top: 14px; width: 225px; height: 230px; background: linear-gradient(100deg, #2e5b8e 0%, #e6e3d8 40%, #1f3a6b 70%, #d23d2b 100%); }

  .special-ribbon { position: absolute; z-index: 2; left: 0; top: 0; width: 110px; height: 110px; }
  .special-ribbon text {
    font-family: "Archivo Black", sans-serif; font-size: 19px; fill: var(--white); letter-spacing: .5px;
  }

  .price-badge {
    position: absolute; z-index: 3; left: 128px; top: 190px; width: 148px; height: 70px; border-radius: 50%;
    background: radial-gradient(ellipse at 45% 30%, var(--price-green-light) 0%, var(--price-green-dark) 100%);
    border: 3px solid var(--price-rim);
    box-shadow: 0 2px 4px rgba(0,0,0,.4);
  }
  .price-figure {
    position: absolute; left: 0; right: 0; top: 7px; text-align: center;
    font-family: "Roboto", sans-serif; font-weight: 900;
    font-size: 44px; line-height: 50px; color: var(--white);
    paint-order: stroke fill; -webkit-text-stroke: 6px var(--outline);
  }

  .product-name, .quantity-note {
    position: absolute; z-index: 4; font-family: "Archivo Black", sans-serif;
    color: var(--label-orange); white-space: nowrap;
    paint-order: stroke fill;
  }
  .product-name { left: 10px; top: 154px; font-size: 24px; line-height: 30px; -webkit-text-stroke: 5px var(--outline); }
  .quantity-note { left: 14px; top: 206px; font-size: 17px; line-height: 22px; -webkit-text-stroke: 4px var(--outline); }
</style>
</head>
<body>
<main class="banner-strip">

  <section class="promo-tile">
    <div class="product-visual visual-tent" role="img" aria-label="Photo of a white folded table tent card with printed menu text"></div>
    <svg class="special-ribbon" viewBox="0 0 110 110" aria-hidden="true">
      <polygon points="0,30 30,0 100,0 0,100" fill="var(--ribbon)"/>
      <polygon points="0,100 100,0 104,0 0,104" fill="var(--ribbon-dark)"/>
      <text x="46" y="45" text-anchor="middle" transform="rotate(-45 46 45)">SPECIAL</text>
    </svg>
    <div class="price-badge"><span class="price-figure">$217</span></div>
    <h2 class="product-name">Table Tents</h2>
    <p class="quantity-note">1000 for</p>
  </section>

  <section class="promo-tile">
    <div class="product-visual visual-flyers" role="img" aria-label="Photo of a fanned stack of colourful event flyers"></div>
    <svg class="special-ribbon" viewBox="0 0 110 110" aria-hidden="true">
      <polygon points="0,30 30,0 100,0 0,100" fill="var(--ribbon)"/>
      <polygon points="0,100 100,0 104,0 0,104" fill="var(--ribbon-dark)"/>
      <text x="46" y="45" text-anchor="middle" transform="rotate(-45 46 45)">SPECIAL</text>
    </svg>
    <div class="price-badge"><span class="price-figure">$328</span></div>
    <h2 class="product-name">Flyers</h2>
    <p class="quantity-note">5000 for</p>
  </section>

  <section class="promo-tile">
    <div class="product-visual visual-postcards" role="img" aria-label="Photo of scattered landscape and sunset postcards"></div>
    <svg class="special-ribbon" viewBox="0 0 110 110" aria-hidden="true">
      <polygon points="0,30 30,0 100,0 0,100" fill="var(--ribbon)"/>
      <polygon points="0,100 100,0 104,0 0,104" fill="var(--ribbon-dark)"/>
      <text x="46" y="45" text-anchor="middle" transform="rotate(-45 46 45)">SPECIAL</text>
    </svg>
    <div class="price-badge"><span class="price-figure">$237</span></div>
    <h2 class="product-name">Postcards</h2>
    <p class="quantity-note">5000 for</p>
  </section>

  <section class="promo-tile">
    <div class="product-visual visual-brochures" role="img" aria-label="Photo of three standing tri-fold brochures"></div>
    <svg class="special-ribbon" viewBox="0 0 110 110" aria-hidden="true">
      <polygon points="0,30 30,0 100,0 0,100" fill="var(--ribbon)"/>
      <polygon points="0,100 100,0 104,0 0,104" fill="var(--ribbon-dark)"/>
      <text x="46" y="45" text-anchor="middle" transform="rotate(-45 46 45)">SPECIAL</text>
    </svg>
    <div class="price-badge"><span class="price-figure">$386</span></div>
    <h2 class="product-name">Brochures</h2>
    <p class="quantity-note">5000 for</p>
  </section>

</main>
</body>
</html>
```